professional business card design

Business card design. Photos have been uploaded and i am open to the designer choosing which photos to use. Would like the card to be mostyly in a grey scale design with black, whites, silver & grey colours. I have added copy of our flyer as would like on the back side of card our services to be listed. Do not use any bright colurs such as blue red green or yellow. i need to be able to edit the phone number and naem in the final card design submitted.

Target Market(s)

Clients

Industry/Entity Type

earhmovibng and transport

Contact Information for Business Card

Director Name, address, email, phone number and services

Colors

Designer to choose only greyscale colors for use in the design.

Requirements
Should not have
• no yellow, red, blue or green

```html
<!DOCTYPE html>
<html lang="en">
<head>
<meta charset="utf-8">
<title>KELDAR Pty Ltd – Business Card</title>
<link href="https://fonts.googleapis.com/css2?family=Poppins:wght@400;500;700;800&display=swap" rel="stylesheet">
<style>
:root{
  --page:#2a2a2b;
  --card:#1b1b1c;
  --card-hi:#3a3a3c;
  --gold:#b0894f;
  --gold-dark:#8a6a3a;
  --white:#f2f2f2;
  --silver:#c9c9cc;
  --muted:#9a9a9e;
}
*{margin:0;padding:0;box-sizing:border-box}
html,body{width:1200px;height:910px;overflow:hidden;background:var(--page);font-family:'Poppins',sans-serif}
.card{position:absolute;left:250px;width:700px;height:400px;border-radius:26px;overflow:hidden;
  background:radial-gradient(ellipse at 62% 30%,var(--card-hi) 0%,#242426 40%,var(--card) 80%);
  box-shadow:0 14px 30px rgba(0,0,0,.45)}
.card--front{top:40px}
.card--back{top:470px}
.photo-fleet{position:absolute;left:0;top:20px;width:420px;height:250px;
  background:linear-gradient(180deg,rgba(90,90,92,.35),rgba(50,50,52,.15) 70%,transparent);
  border-radius:0 0 60% 0}
.brand{position:absolute;color:var(--silver);font-weight:800;letter-spacing:2px;display:flex;align-items:center;gap:10px}
.brand__dot{width:14px;height:14px;border-radius:50%;background:var(--silver)}
.card--front .brand{left:330px;top:70px;font-size:40px}
.card--back .brand{left:380px;top:40px;font-size:38px}
.name-band{position:absolute;left:0;top:130px;width:52px;height:30px;background:var(--gold);
  clip-path:polygon(0 0,100% 0,85% 100%,0 100%);display:flex;align-items:center;justify-content:center}
.person{position:absolute;left:62px;top:124px;color:var(--white)}
.person__name{font-size:28px;font-weight:400;line-height:1.1}
.person__name b{font-weight:800}
.person__role{font-size:12px;letter-spacing:1px;color:var(--silver)}
.contact{position:absolute;left:410px;top:250px}
.contact__line{position:absolute;left:12px;top:14px;width:2px;height:110px;background:var(--gold)}
.contact__item{position:relative;display:flex;align-items:flex-start;gap:14px;margin-bottom:12px;color:var(--white);font-size:15px;line-height:1.25}
.contact__icon{flex:none;width:26px;height:26px;background:var(--gold);transform:rotate(45deg);border-radius:4px;display:flex;align-items:center;justify-content:center}
.contact__icon svg{transform:rotate(-45deg)}
.services-title{position:absolute;left:300px;top:150px;color:var(--white);font-size:34px;font-weight:800;letter-spacing:1px}
.service-list{position:absolute;list-style:none}
.service-list li{background:linear-gradient(90deg,var(--gold),var(--gold-dark));color:var(--white);font-size:12.5px;line-height:1.35;
  padding:3px 22px 3px 12px;margin-bottom:5px;clip-path:polygon(0 0,100% 0,94% 100%,0 100%);white-space:nowrap}
.service-list li::before{content:"";display:inline-block;width:6px;height:6px;border:1.5px solid var(--white);border-radius:50%;margin-right:7px;vertical-align:1px}
.service-list--left{left:0;top:96px}
.service-list--right{left:300px;top:206px;width:225px}
.service-list--right li{white-space:normal}
.photo-truck{position:absolute;right:0;bottom:0;width:165px;height:165px;
  background:linear-gradient(160deg,#8d8e91,#cfcfd2 45%,#6d6a63 80%,#3a3936);border-top-left-radius:40px}
</style>
</head>
<body>

<section class="card card--front">
  <div class="photo-fleet" role="img" aria-label="Faded photo of a fleet of road train trucks"></div>
  <div class="brand"><span class="brand__dot"></span>KELDAR</div>
  <div class="name-band">
    <svg width="14" height="14" viewBox="0 0 14 14"><circle cx="7" cy="4" r="3" fill="#fff"/><path d="M1 14c0-4 3-6 6-6s6 2 6 6z" fill="#fff"/></svg>
  </div>
  <div class="person">
    <p class="person__name"><b>Daniel</b> Brooks</p>
    <p class="person__role">DIRECTOR</p>
  </div>
  <div class="contact">
    <div class="contact__line"></div>
    <div class="contact__item">
      <span class="contact__icon"><svg width="12" height="12" viewBox="0 0 12 12"><path d="M2 1l2 0 1 3-1.5 1a7 7 0 003.5 3.5L8 7l3 1v2c0 1-1 1-1 1C5 11 1 7 1 2c0 0 0-1 1-1z" fill="#fff"/></svg></span>
      <span>000 111 222 333</span>
    </div>
    <div class="contact__item">
      <span class="contact__icon"><svg width="12" height="12" viewBox="0 0 12 12"><rect x="1" y="2.5" width="10" height="7" rx="1" fill="none" stroke="#fff" stroke-width="1.3"/><path d="M1.5 3l4.5 3.5L10.5 3" fill="none" stroke="#fff" stroke-width="1.3"/></svg></span>
      <span>office@keldarhaul.com</span>
    </div>
    <div class="contact__item">
      <span class="contact__icon"><svg width="12" height="12" viewBox="0 0 12 12"><path d="M6 11S2 7 2 4.5a4 4 0 018 0C10 7 6 11 6 11z" fill="#fff"/><circle cx="6" cy="4.5" r="1.4" fill="#b0894f"/></svg></span>
      <span>14 Quarry Road<br>Stonebridge, WA - 000</span>
    </div>
  </div>
</section>

<section class="card card--back">
  <div class="photo-fleet" role="img" aria-label="Faded photo of road train trucks"></div>
  <div class="brand"><span class="brand__dot"></span>KELDAR</div>
  <ul class="service-list service-list--left">
    <li>Over size loads / Hot Shot Load</li>
    <li>Heavy Vehicle Recovery Services</li>
    <li>Potable Water Deliveries</li>
    <li>Road Building / Maintenance</li>
    <li>Earthworks</li>
    <li>Sand &amp; Metal Supply &amp; Cartage</li>
  </ul>
  <h2 class="services-title">OUR SERVICES</h2>
  <ul class="service-list service-list--right">
    <li>Road Train Tippers</li>
    <li>Road Train Tankers</li>
    <li>Road Train Flat Tops</li>
    <li>Drop Deck Trailers</li>
    <li>Mine Site accredited equipment &amp; Operators</li>
  </ul>
  <div class="photo-truck" role="img" aria-label="Photo of a white road train truck front"></div>
</section>

</body>
</html>
```